KESTRA Communications Business Card- Olde

Kestra Integrated Communications is Corporate communications agency with more than 20 years of experience. We become part of the manegement team of our clients in other to improve their outcomes and grow the possitioning of their brand.
We are in Puerto Rico, latin caribbean island
Name: Marisolde (Olde) Fuentes
787-555-0148
ofuentes@kestrakom.example

Target Market(s)

finance and pharmaceutical companies

Industry/Entity Type

Business

Contact Information for Business Card

modern, edgy colorful and playfull like our logo

Requirements
Must have
• company logo
• name
• tel
• email

```html
<!DOCTYPE html>
<html lang="en">
<head>
<meta charset="utf-8">
<title>Kestra Integrated Communications – Business Card</title>
<link rel="stylesheet" href="https://fonts.googleapis.com/css2?family=Arimo:wght@400;700&display=swap">
<style>
  :root {
    --backdrop: #2b2b2b;
    --card-white: #f7f7f7;
    --brand-orange: #e0561f;
    --brand-brown: #3a2a0e;
    --ink-dark: #1f1a12;
    --ink-light: #f2efe9;
    --font-main: "Arimo", Arial, sans-serif;
  }
  * { box-sizing: border-box; margin: 0; padding: 0; }
  html, body {
    width: 1200px; height: 997px; overflow: hidden;
    background: var(--backdrop);
    font-family: var(--font-main);
  }
  .stage {
    width: 1200px; height: 997px;
    display: flex; flex-direction: column;
    align-items: center; justify-content: center; gap: 40px;
  }
  .card {
    position: relative;
    width: 760px; height: 434px;
    background: var(--card-white);
    overflow: hidden;
    box-shadow: 0 8px 24px rgba(0,0,0,.45);
  }
  .card-shapes { position: absolute; inset: 0; width: 100%; height: 100%; }
  .brand-name {
    position: absolute;
    color: var(--brand-brown);
    font-weight: 700;
    line-height: 1.1;
    text-align: center;
  }
  .brand-name .word { display: block; font-size: 54px; letter-spacing: 4px; }
  .brand-name .tagline { display: block; font-size: 13px; letter-spacing: 2px; margin-top: 4px; }

  /* back side */
  .card-back .brand-name { left: 250px; top: 70px; }
  .social-handle {
    position: absolute; left: 70px; top: 336px;
    display: flex; align-items: center; gap: 10px;
    color: var(--ink-light); font-size: 18px; line-height: 1;
  }
  .social-handle .marker { width: 20px; height: 20px; background: var(--ink-light); }
  .website {
    position: absolute; right: 36px; bottom: 30px;
    color: var(--ink-light); font-size: 20px; letter-spacing: 3px;
  }

  /* front side */
  .card-front .brand-name { right: 50px; top: 50px; }
  .person-name {
    position: absolute; left: 40px; top: 150px;
    color: var(--ink-dark); font-size: 25px; font-weight: 700; line-height: 1.2;
  }
  .address {
    position: absolute; right: 34px; top: 292px;
    color: var(--ink-light); font-size: 18px; line-height: 1.3; text-align: right;
  }
  .contact-list {
    position: absolute; left: 60px; top: 345px;
    list-style: none; color: var(--ink-light); font-size: 21px; line-height: 1.2;
  }
  .contact-list li { display: flex; align-items: center; gap: 18px; margin-bottom: 12px; }
  .contact-list svg { width: 20px; height: 20px; flex: none; }
</style>
</head>
<body>
<main class="stage">

  <section class="card card-back" aria-label="Business card back">
    <svg class="card-shapes" viewBox="0 0 760 434" preserveAspectRatio="none" aria-hidden="true">
      <path d="M0,316 Q420,290 690,0 L745,0 Q465,340 0,384 Z" fill="var(--brand-orange)"/>
      <path d="M0,394 Q475,352 756,0 L760,0 L760,434 L0,434 Z" fill="var(--brand-brown)"/>
    </svg>
    <div class="brand-name">
      <span class="word">KESTRA</span>
      <span class="tagline">INTEGRATED COMMUNICATIONS</span>
    </div>
    <div class="social-handle"><span class="marker"></span>/olde</div>
    <div class="website">www.kestrakom.example</div>
  </section>

  <section class="card card-front" aria-label="Business card front">
    <svg class="card-shapes" viewBox="0 0 760 434" preserveAspectRatio="none" aria-hidden="true">
      <path d="M0,238 Q360,262 760,140 L760,168 Q370,305 0,282 Z" fill="var(--brand-orange)"/>
      <path d="M0,292 Q370,315 760,178 L760,434 L0,434 Z" fill="var(--brand-brown)"/>
    </svg>
    <div class="brand-name">
      <span class="word">KESTRA</span>
      <span class="tagline">INTEGRATED COMMUNICATIONS</span>
    </div>
    <p class="person-name">Marisolde (Olde)<br>Fuentes</p>
    <p class="address">27 Palm Grove Road, Hacienda Las Brisas<br>Caguas, Puerto Rico 00725</p>
    <ul class="contact-list">
      <li>
        <svg viewBox="0 0 20 20" aria-hidden="true"><rect x="4" y="1.5" width="12" height="17" rx="2" fill="none" stroke="var(--brand-orange)" stroke-width="2"/></svg>
        787-555-0148
      </li>
      <li>
        <svg viewBox="0 0 20 20" aria-hidden="true"><rect x="1" y="4" width="18" height="12" fill="var(--brand-orange)"/><path d="M1,4 L10,11 L19,4" fill="none" stroke="var(--brand-brown)" stroke-width="1.5"/></svg>
        ofuentes@kestrakom.example
      </li>
    </ul>
  </section>

</main>
</body>
</html>
```